WAGLH - 2020 Vision Banner

3 x 6-foot banner
For a Christian Church, a Theme designed Banner for 2020

Target Market(s)

Christian Congregation, internal church banner

Industry/Entity Type

Church

Font styles to use
Decorative

Colors
886aae
ffffff

Requirements
Must have
• Word-Anchored Gathering Church of Larkmoor Heights
• 2020 Vision
• Use Logo
• Color Combinations are: white, black, purple, sliver
• Communicate faith, future, and hope
Nice to have
• Bible
• Cross
Should not have
• No clip art

```html
<!DOCTYPE html>
<html lang="en">
<head>
<meta charset="utf-8">
<title>WAGLH – 2020 Vision Banner</title>
<link href="https://fonts.googleapis.com/css2?family=Exo+2:wght@900&family=Barlow:wght@500;600;700&display=swap" rel="stylesheet">
<style>
  :root {
    --backdrop: #c8c8c8;
    --purple: #663399;
    --purple-deep: #4e2479;
    --white: #ffffff;
    --silver-light: #f4f4f4;
    --silver-mid: #b9b9b9;
    --silver-dark: #7d7d7d;
    --ink: #1a1a1a;
  }
  * { margin: 0; padding: 0; box-sizing: border-box; }
  html, body {
    width: 1200px; height: 917px; overflow: hidden;
    background: var(--backdrop);
  }
  .banner {
    position: absolute; left: 109px; top: 213px;
    width: 981px; height: 491px;
    background: var(--purple);
    overflow: hidden;
  }
  .banner-art { position: absolute; inset: 0; }
  .church-mark {
    position: absolute; left: 24px; top: 17px;
    width: 88px; height: 88px; border-radius: 50%;
    background: var(--ink);
    display: flex; align-items: center; justify-content: center;
    font-family: "Barlow", sans-serif; font-weight: 700;
    font-size: 19px; color: var(--white); letter-spacing: 0.5px;
  }
  .church-name {
    position: absolute; left: 154px; top: 42px;
    font-family: "Barlow", sans-serif; font-weight: 700;
    font-size: 17px; line-height: 21px;
    color: var(--white); text-transform: uppercase; letter-spacing: 0.2px;
  }
  .theme-title {
    position: absolute; left: 24px; top: 128px;
    font-family: "Exo 2", sans-serif; font-weight: 900;
    font-size: 134px; line-height: 122px; letter-spacing: 1px;
    background: linear-gradient(180deg, var(--silver-light) 0%, var(--silver-mid) 45%, var(--silver-dark) 55%, var(--silver-light) 100%);
    -webkit-background-clip: text; background-clip: text;
    color: transparent;
  }
  .theme-title span { display: block; }
  .theme-tagline {
    position: absolute; left: 30px; top: 383px;
    font-family: "Barlow", sans-serif; font-weight: 600;
    font-size: 37px; color: var(--white); letter-spacing: 0.2px;
  }
  .web-address {
    position: absolute; left: 30px; top: 444px;
    font-family: "Barlow", sans-serif; font-weight: 500;
    font-size: 21px; color: var(--white);
  }
</style>
</head>
<body>
  <main class="banner">
    <svg class="banner-art" width="981" height="491" viewBox="0 0 981 491">
      <defs>
        <linearGradient id="silverRing" x1="0" y1="0" x2="1" y2="1">
          <stop offset="0" stop-color="#f2f2f2"/>
          <stop offset="0.5" stop-color="#9a9a9a"/>
          <stop offset="1" stop-color="#e6e6e6"/>
        </linearGradient>
        <linearGradient id="purpleRing" x1="0" y1="0" x2="0" y2="1">
          <stop offset="0" stop-color="#8a64b8"/>
          <stop offset="1" stop-color="#4e2479"/>
        </linearGradient>
        <radialGradient id="photoTone" cx="0.55" cy="0.45" r="0.7">
          <stop offset="0" stop-color="#f2f2f2"/>
          <stop offset="0.6" stop-color="#bcbcbc"/>
          <stop offset="1" stop-color="#5a5a5a"/>
        </radialGradient>
      </defs>
      <circle cx="815" cy="110" r="392" fill="url(#silverRing)"/>
      <circle cx="815" cy="110" r="383" fill="url(#purpleRing)"/>
      <circle cx="815" cy="110" r="372" fill="url(#photoTone)" role="img"
        aria-label="Black and white photograph of a crucifix against a pale sky, with a raised hand holding up a Holy Bible"/>
    </svg>

    <div class="church-mark">WAGLH</div>
    <h1 class="church-name">Word-Anchored Gathering Church<br>of Larkmoor Heights</h1>

    <h2 class="theme-title"><span>2020</span><span>VISION</span></h2>
    <p class="theme-tagline">FAITH, FUTURE AND HOPE</p>
    <p class="web-address">www.waglh.org</p>
  </main>
</body>
</html>
```